Nutrition product information web site

Nutrition Website (see upload) without Shop function but link to Brivel ASIN number that customer could order from Brivel direct. Content must be easily editable without coding. Web environment must be responsive to support mobile devices as well. design should be modern and clear. loading of web elements must be fast. not too much time consuming features.

Industry/Entity Type

Nutrition

Number of Pages Required

5+ page

Font styles to use
Sans Serif

Colors
33b8a4
9bcb3c
0255a3
0a90cc
a54499

Requirements
Must have
• read attached document
Nice to have
• read attached document
Should not have
• read attached document

```html
<!DOCTYPE html>
<html lang="en">
<head>
<meta charset="utf-8">
<title>Velora – Well Being Through Smart Research</title>
<link href="https://fonts.googleapis.com/css2?family=Open+Sans:ital,wght@0,400;0,600;0,700;0,800;1,400&display=swap" rel="stylesheet">
<style>
:root{
  --teal:#17bcc6;
  --teal-dark:#119aa3;
  --ink:#222;
  --text:#555;
  --muted:#888;
  --dark:#1d1d1d;
  --white:#fff;
  --grey-card:#d8d8d8;
}
*{box-sizing:border-box;margin:0;padding:0}
html,body{width:1200px;height:3226px;overflow:hidden}
body{font-family:"Open Sans",Arial,sans-serif;color:var(--text);background:var(--white);position:relative}
a{color:inherit;text-decoration:none}

/* Header */
.site-header{position:absolute;top:0;left:0;width:1200px;height:99px;background:var(--white)}
.topbar{position:absolute;right:0;top:0;width:700px;height:32px;background:var(--dark);color:#eee;font-size:11px;display:flex;align-items:center;gap:40px;padding-left:30px;clip-path:polygon(20px 0,100% 0,100% 100%,0 100%)}
.topbar .lang{margin-left:auto;margin-right:30px}
.brand{position:absolute;left:282px;top:8px;display:flex;flex-direction:column;align-items:center;gap:6px}
.brand .dot{width:46px;height:46px;border-radius:50%;border:3px solid var(--teal)}
.brand .name{font-weight:700;font-size:20px;letter-spacing:5px;color:var(--ink)}
.main-nav{position:absolute;left:510px;top:58px;display:flex;gap:12px;font-size:11px;color:var(--ink);white-space:nowrap}
.main-nav a.active{color:var(--teal);font-weight:600}
.btn-login{position:absolute;left:862px;top:50px;width:88px;height:32px;background:var(--teal);color:var(--white);font-weight:700;font-size:11px;display:flex;align-items:center;justify-content:center}

/* Hero */
.hero{position:absolute;top:99px;left:0;width:1200px;height:445px;background:linear-gradient(135deg,#6b4a2e 0%,#9a7048 45%,#7b5636 100%)}
.hero-shade{position:absolute;inset:0;background:rgba(0,0,0,.25)}
.hero-copy{position:absolute;left:280px;top:120px;width:666px;text-align:center;color:var(--white)}
.hero-copy h1{font-weight:800;font-size:46px;line-height:46px;text-transform:uppercase}
.hero-copy p{font-size:13px;line-height:20px;width:510px;margin:6px auto 0}
.btn{display:inline-flex;align-items:center;justify-content:center;background:var(--teal);color:var(--white);font-weight:600;font-size:12px}
.hero .btn{position:absolute;left:531px;top:264px;width:142px;height:43px}

/* About */
.about{position:absolute;top:544px;left:0;width:1200px;height:387px;background:var(--white)}
.about h2{position:absolute;left:249px;top:90px;font-weight:800;font-size:38px;color:var(--teal)}
.about .lead{position:absolute;left:249px;top:140px;width:360px;font-size:17px;line-height:24px;color:#444}
.about .body{position:absolute;left:249px;top:198px;width:340px;font-size:11px;line-height:18px;color:var(--muted)}
.about .btn{position:absolute;left:249px;top:279px;width:144px;height:42px}
.about-photo{position:absolute;left:651px;top:54px;width:282px;height:282px;border-radius:50%;border:12px solid #1e1e1e;background:radial-gradient(circle at 50% 45%,#ffffff 0%,#eef1f4 55%,#c9d3dc 100%)}

/* Products */
.products{position:absolute;top:931px;left:0;width:1200px;height:553px;background:var(--teal);color:var(--white);text-align:center}
.products h2,.testimonials h2{font-weight:800;font-size:36px;padding-top:40px}
.products .intro{font-size:13px;line-height:20px;width:360px;margin:6px auto 0}
.product-card{position:absolute;top:166px;width:226px;height:340px;background:var(--grey-card);border:4px solid var(--white);box-shadow:0 4px 12px rgba(0,0,0,.2);color:var(--ink)}
.product-card .shot{height:220px;background:linear-gradient(180deg,#cfcfcf,#e6e6e6)}
.product-card h3{font-size:11px;font-weight:800;margin-top:8px}
.product-card p{font-size:9px;line-height:13px;width:170px;margin:4px auto 0}
.product-card .cart{display:inline-flex;align-items:center;justify-content:center;margin-top:12px;width:100px;height:28px;background:var(--dark);color:var(--white);font-size:9px;font-weight:700}

/* Features */
.features{position:absolute;top:1484px;left:0;width:1200px;height:458px;background:var(--white)}
.feature-photo{position:absolute;border-radius:50%;box-shadow:0 6px 18px rgba(0,0,0,.18)}
.feature h3{position:absolute;width:230px;text-align:center;font-weight:800;font-size:14px;color:var(--ink);text-transform:uppercase}
.feature p{position:absolute;width:200px;text-align:center;font-size:9px;line-height:13px;color:var(--text)}

/* Testimonials */
.testimonials{position:absolute;top:1942px;left:0;width:1200px;height:424px;background:var(--teal);color:var(--white);text-align:center}
.testimonials h2{padding-top:44px;line-height:38px}
.testimonials .kicker{font-size:13px;letter-spacing:5px;text-transform:uppercase}
.testimonials .rule{width:40px;height:2px;background:var(--white);margin:10px auto 0}
.avatar{position:absolute;left:540px;top:146px;width:118px;height:118px;border-radius:50%;border:4px solid var(--white);background:linear-gradient(160deg,#e7e2dc,#9a8f86)}
.client{position:absolute;top:284px;width:1200px;font-size:11px;font-weight:700}
.client small{display:block;font-size:8px;font-weight:400;margin-top:2px}
.quote{position:absolute;left:250px;top:320px;width:700px;font-size:11px;line-height:18px;font-style:italic}
.dots{position:absolute;top:372px;left:570px;display:flex;gap:6px}
.dots span{width:8px;height:8px;border-radius:50%;border:1px solid var(--white)}
.dots span.on{background:var(--white)}

/* Blogs */
.blogs{position:absolute;top:2366px;left:0;width:1200px;height:554px;background:var(--white);text-align:center}
.blogs h2{font-weight:800;font-size:34px;color:var(--teal);padding-top:50px}
.blogs .rule{width:40px;height:2px;background:var(--teal);margin:8px auto 0}
.blogs .intro{font-size:13px;line-height:20px;width:380px;margin:12px auto 0;color:#444}
.post{position:absolute;top:171px;width:224px;height:329px;background:var(--white);box-shadow:0 2px 10px rgba(0,0,0,.12);text-align:left}
.post .shot{height:179px}
.post .meta{padding:18px 16px 0;font-size:9px;font-weight:700;color:var(--ink)}
.post h3{padding:4px 16px 0;font-size:12px;line-height:15px;color:var(--teal);font-weight:700}
.post .by{padding:4px 16px 0;font-size:8px;color:var(--muted)}
.post p{padding:8px 16px 0;font-size:8px;line-height:11px;color:#999}
.post .more{padding:10px 16px 0;font-size:8px;font-weight:700;color:var(--ink)}

/* Footer */
.site-footer{position:absolute;top:2920px;left:0;width:1200px;height:267px;background:var(--dark);color:#ddd}
.footer-col{position:absolute;top:42px}
.footer-col h4{font-size:14px;font-weight:800;color:var(--white);text-transform:uppercase}
.footer-col h4.brandname{font-size:20px}
.footer-col .rule{width:44px;height:2px;background:var(--white);margin:8px 0 12px}
.footer-col p{font-size:9px;line-height:14px}
.links li{list-style:none;font-size:11px;line-height:21px}
.links li::before{content:"› ";color:var(--white)}
.contact-row{display:flex;gap:10px;font-size:9px;line-height:13px;margin-bottom:12px}
.contact-row .ico{flex:0 0 18px;height:18px;background:var(--teal);display:flex;align-items:center;justify-content:center}
.social{display:flex;gap:6px;margin-top:12px}
.social span{width:22px;height:22px;border-radius:50%;background:var(--teal)}
.newsletter{display:flex;margin-top:14px}
.newsletter .field{width:150px;height:28px;background:var(--white);color:#999;font-size:9px;display:flex;align-items:center;padding-left:8px}
.newsletter .send{width:30px;height:28px;background:var(--teal);display:flex;align-items:center;justify-content:center}
.copyright{position:absolute;top:3187px;left:0;width:1200px;height:39px;background:var(--teal);color:var(--white);font-size:9px;display:flex;align-items:center;padding-left:249px}
</style>
</head>
<body>

<header class="site-header">
  <div class="topbar">
    <span>Phone Number: +43 600 100 2000</span>
    <span>Email: hello@veloralabs.com</span>
    <span class="lang">Eng ▾</span>
  </div>
  <a class="brand" href="#"><span class="dot"></span><span class="name">VELORA</span></a>
  <nav class="main-nav">
    <a class="active" href="#">Home</a><a href="#">About us</a><a href="#">Products</a><a href="#">Blog</a><a href="#">Testimonials</a><a href="#">Contact us</a>
  </nav>
  <a class="btn-login" href="#">LOG IN</a>
</header>

<section class="hero" role="img" aria-label="Flat lay of fitness items, fruit and a tablet on a wooden table">
  <div class="hero-shade"></div>
  <div class="hero-copy">
    <h1>Well Being<br>Through Smart Research</h1>
    <p>Lorem Ipsum is simply dummy text of the printing and typesetting industry. Lorem Ipsum has been the industry's standard dummy text ever since the 1500s.</p>
  </div>
  <a class="btn" href="#">Read More</a>
</section>

<section class="about">
  <h2>ABOUT VELORA</h2>
  <p class="lead">Lorem Ipsum is simply dummy text of the printing and typesetting industry.</p>
  <p class="body">Lorem Ipsum is simply dummy text of the printing and typesetting industry. Lorem Ipsum has been the industry's standard dummy text ever since the 1500s, when an unknown printer took a galley of type and scrambled it to make a type specimen book.</p>
  <a class="btn" href="#">Read More</a>
  <div class="about-photo" role="img" aria-label="White supplement bottle with blue label"></div>
</section>

<section class="products">
  <h2>OUR PRODUCTS</h2>
  <p class="intro">Lorem Ipsum is simply dummy text of the printing and typesetting industry. Lorem Ipsum has been the industry's</p>
  <article class="product-card" style="left:249px">
    <div class="shot" role="img" aria-label="Seda Mono supplement bottle with green accent"></div>
    <h3>SEDA MONO</h3>
    <p>Lorem Ipsum is simply dummy text of the printing and typesetting industry.</p>
    <a class="cart" href="#">ADD TO CART</a>
  </article>
  <article class="product-card" style="left:490px">
    <div class="shot" role="img" aria-label="B Complete supplement bottle with blue accent"></div>
    <h3>B COMPLETE</h3>
    <p>Lorem Ipsum is simply dummy text of the printing and typesetting industry.</p>
    <a class="cart" href="#">ADD TO CART</a>
  </article>
  <article class="product-card" style="left:729px">
    <div class="shot" role="img" aria-label="Leaf Focus supplement bottle with teal accent"></div>
    <h3>LEAF FOCUS</h3>
    <p>Lorem Ipsum is simply dummy text of the printing and typesetting industry.</p>
    <a class="cart" href="#">ADD TO CART</a>
  </article>
</section>

<section class="features">
  <div class="feature">
    <div class="feature-photo" style="left:245px;top:101px;width:206px;height:206px;background:linear-gradient(135deg,#e9e4dc,#b9c4cf)" role="img" aria-label="Happy couple cheering"></div>
    <h3 style="left:233px;top:350px">Smart Living</h3>
    <p style="left:248px;top:372px">Lorem Ipsum is simply dummy text of the printing and typesetting industry. Lorem Ipsum has been the industry's</p>
  </div>
  <div class="feature">
    <div class="feature-photo" style="left:469px;top:68px;width:258px;height:258px;border:6px solid var(--teal);background:linear-gradient(135deg,#f3efe6,#e8c64a)" role="img" aria-label="Woman eating a healthy salad"></div>
    <h3 style="left:483px;top:350px">Smart Dieting</h3>
    <p style="left:498px;top:372px">Lorem Ipsum is simply dummy text of the printing and typesetting industry. Lorem Ipsum has been the industry's</p>
  </div>
  <div class="feature">
    <div class="feature-photo" style="left:740px;top:101px;width:206px;height:206px;background:linear-gradient(135deg,#8fd3e3,#3b8fb8)" role="img" aria-label="Man running by the sea"></div>
    <h3 style="left:728px;top:350px">Smart Body</h3>
    <p style="left:743px;top:372px">Lorem Ipsum is simply dummy text of the printing and typesetting industry. Lorem Ipsum has been the industry's</p>
  </div>
</section>

<section class="testimonials">
  <h2>TESTIMONIALS</h2>
  <div class="kicker">What our clients say</div>
  <div class="rule"></div>
  <div class="avatar" role="img" aria-label="Portrait of client Mara Lind"></div>
  <div class="client">MARA LIND<small>Web Designer</small></div>
  <p class="quote">Lorem ipsum dolor sit amet, consectetur adipiscing elit, sed do eiusmod tempor incididunt ut labore et dolore magna aliqua. Ut enim ad minim veniam, quis nostrud exercitation ullamco laboris nisi ut aliquip ex ea commodo consequat.</p>
  <div class="dots"><span class="on"></span><span></span><span></span><span></span></div>
</section>

<section class="blogs">
  <h2>BLOGS</h2>
  <div class="rule"></div>
  <p class="intro">Lorem Ipsum is simply dummy text of the printing and typesetting industry. Lorem Ipsum has been the industry's</p>
  <article class="post" style="left:249px">
    <div class="shot" style="background:linear-gradient(135deg,#e8edf2,#3a4a5e)" role="img" aria-label="Business people reviewing documents"></div>
    <div class="meta">DECEMBER 13, 2017</div>
    <h3>Lorem Ipsum is simply dummy text of the printing</h3>
    <div class="by">By Admin</div>
    <p>Lorem Ipsum is simply dummy text of the printing and typesetting industry. Lorem Ipsum has been the industry's</p>
    <div class="more">› READ MORE</div>
  </article>
  <article class="post" style="left:489px">
    <div class="shot" style="background:linear-gradient(135deg,#f6c27a,#7a3f2a)" role="img" aria-label="Woman in warm sunlight"></div>
    <div class="meta">DECEMBER 19, 2017</div>
    <h3>Lorem Ipsum is simply dummy text of the printing</h3>
    <div class="by">By Admin</div>
    <p>Lorem Ipsum is simply dummy text of the printing and typesetting industry. Lorem Ipsum has been the industry's</p>
    <div class="more">› READ MORE</div>
  </article>
  <article class="post" style="left:729px">
    <div class="shot" style="background:linear-gradient(135deg,#efe9e2,#b5483e)" role="img" aria-label="Woman working on a laptop"></div>
    <div class="meta">DECEMBER 10, 2017</div>
    <h3>Lorem Ipsum is simply dummy text of the printing</h3>
    <div class="by">By Admin</div>
    <p>Lorem Ipsum is simply dummy text of the printing and typesetting industry. Lorem Ipsum has been the industry's</p>
    <div class="more">› READ MORE</div>
  </article>
</section>

<footer class="site-footer">
  <div class="footer-col" style="left:249px;width:200px">
    <h4 class="brandname">VELORA.CO</h4>
    <p style="margin-top:12px">Lorem Ipsum is simply dummy text of the printing and typesetting industry. Lorem Ipsum has been the industry's standard dummy text ever since the 1500s.</p>
    <h4 style="margin-top:14px">Stay Connected</h4>
    <div class="rule" style="margin-bottom:0"></div>
    <div class="social"><span></span><span></span><span></span><span></span><span></span><span></span></div>
  </div>
  <div class="footer-col" style="left:465px">
    <h4>Link</h4>
    <div class="rule"></div>
    <ul class="links"><li>Home</li><li>About us</li><li>Product</li><li>Testimonials</li><li>Blog</li><li>Contact us</li></ul>
  </div>
  <div class="footer-col" style="left:576px;width:180px">
    <h4>Contact Us</h4>
    <div class="rule"></div>
    <div class="contact-row"><span class="ico"><svg width="10" height="12" viewBox="0 0 10 12"><path d="M5 0a4 4 0 0 0-4 4c0 3 4 8 4 8s4-5 4-8a4 4 0 0 0-4-4zm0 5.5A1.5 1.5 0 1 1 5 2.5a1.5 1.5 0 0 1 0 3z" fill="#fff"/></svg></span><span><b>Address</b><br>Velora Research GmbH, Lindenweg 12, 8010 Graz Austria</span></div>
    <div class="contact-row"><span class="ico"><svg width="10" height="10" viewBox="0 0 10 10"><path d="M2 0l2 2-1 1.5a6 6 0 0 0 3.5 3.5L8 6l2 2-1.5 2C4 10 0 6 0 1.5z" fill="#fff"/></svg></span><span><b>Mobile :</b> +43 600 100 2000</span></div>
    <div class="contact-row"><span class="ico"><svg width="11" height="8" viewBox="0 0 11 8"><rect x=".5" y=".5" width="10" height="7" fill="none" stroke="#fff"/><path d="M.5.5l5 4 5-4" fill="none" stroke="#fff"/></svg></span><span><b>Email :</b> hello@veloralabs.com</span></div>
  </div>
  <div class="footer-col" style="left:768px;width:190px">
    <h4>Newsletter</h4>
    <div class="rule"></div>
    <p>Lorem Ipsum is simply dummy text of the printing and typesetting industry.</p>
    <div class="newsletter"><span class="field">Your Email Address</span><span class="send"><svg width="12" height="12" viewBox="0 0 12 12"><path d="M0 5l12-5-4 12-2-5z" fill="#fff"/></svg></span></div>
  </div>
</footer>
<div class="copyright">Copyright © 2017 VELORA . All Rights Reserved.</div>

</body>
</html>
```